Sports Therapy and Personal Training

I need a business card design for a new business based in Toronto called "Holbrin Athletics" I am a sports therapist as well as a strength and conditioning coach, therefore I work mainly with high level athletes and physically active people. I am starting my own therapy/training business. The services I will be offering include fitness consultation, personal training, athlete assessments, and rehabilitation therapy. These services will be delivered in peoples homes and/or a facility in which I rent space.

The final design should communicate "high-end" and "quality"

Target Market(s)

athletes and physically active people

Industry/Entity Type

Fitness

Requirements
Must have
• 1. The business logo - files attached

2. my name and credentials

Derek Falloway - CAT(C), CK, CSCS,

Certified Athletic Therapist
Strength and Conditioning Specialist

3. website - www.holbrinathletics.example

4. email address - derek@holbrinathletics.example

5. phone number

```html
<!DOCTYPE html>
<html lang="en">
<head>
<meta charset="UTF-8">
<title>Holbrin Athletics – Business Card</title>
<link rel="stylesheet" href="https://fonts.googleapis.com/css2?family=Gruppo&display=swap">
<style>
  :root {
    --page-bg: #ffffff;
    --card-light: #f2f2f2;
    --card-mid: #bdbdbd;
    --card-lower-top: #8e8e8e;
    --card-lower-bottom: #6a6a6a;
    --band-dark: #3a3a3a;
    --accent-red: #d52b2b;
    --ink: #2e2e2e;
  }
  * { margin: 0; padding: 0; box-sizing: border-box; }
  html, body {
    width: 1200px;
    height: 900px;
    overflow: hidden;
    background: var(--page-bg);
  }
  .business-card {
    position: absolute;
    left: 0;
    top: 108px;
    width: 1200px;
    height: 684px;
    font-family: "Gruppo", "Helvetica Neue", Arial, sans-serif;
    color: var(--ink);
    text-transform: uppercase;
  }
  .card-shapes {
    position: absolute;
    inset: 0;
    display: block;
  }
  .brand-mark {
    position: absolute;
    left: 34px;
    top: 74px;
    display: flex;
    align-items: center;
    gap: 16px;
    font-size: 34px;
    font-weight: 400;
    letter-spacing: 2px;
    color: var(--ink);
  }
  .brand-square {
    width: 34px;
    height: 34px;
    background: var(--accent-red);
  }
  .card-details {
    position: absolute;
    right: 20px;
    top: 262px;
    text-align: right;
    line-height: 1;
  }
  .company-name {
    font-size: 66px;
    font-weight: 400;
    letter-spacing: 1px;
    margin-bottom: 6px;
  }
  .person-name {
    font-size: 45px;
    margin-bottom: 10px;
  }
  .credential {
    font-size: 32px;
    margin-bottom: 8px;
    letter-spacing: 0.5px;
  }
  .contact-list {
    list-style: none;
    margin-top: 50px;
    text-align: left;
    display: inline-block;
  }
  .contact-list li {
    font-size: 32px;
    margin-bottom: 10px;
    letter-spacing: 0.5px;
  }
</style>
</head>
<body>
  <section class="business-card">
    <svg class="card-shapes" width="1200" height="684" viewBox="0 0 1200 684" aria-hidden="true">
      <defs>
        <linearGradient id="upperGradient" x1="0" y1="0" x2="1" y2="1">
          <stop offset="0" stop-color="var(--card-light)"/>
          <stop offset="1" stop-color="var(--card-mid)"/>
        </linearGradient>
        <linearGradient id="lowerGradient" x1="0" y1="0" x2="1" y2="1">
          <stop offset="0" stop-color="var(--card-lower-top)"/>
          <stop offset="1" stop-color="var(--card-lower-bottom)"/>
        </linearGradient>
      </defs>
      <rect class="lower-field" width="1200" height="684" fill="url(#lowerGradient)"/>
      <path class="upper-field" d="M0 0 H1200 V85 C900 95 500 170 0 225 Z" fill="url(#upperGradient)"/>
      <path class="dark-swoosh" d="M0 225 C500 170 900 95 1200 85 V125 C900 140 500 215 0 268 Z" fill="var(--band-dark)"/>
      <path class="red-swoosh" d="M0 268 C500 215 900 140 1200 125" fill="none" stroke="var(--accent-red)" stroke-width="7"/>
    </svg>

    <div class="brand-mark">
      <span class="brand-square"></span>
      <span class="brand-name">Holbrin Athletics</span>
    </div>

    <div class="card-details">
      <h1 class="company-name">Holbrin Athletics</h1>
      <p class="person-name">Derek Falloway - CAT(C), CK, CSCS</p>
      <p class="credential">Certified Athletic Therapist</p>
      <p class="credential">Strength and Conditioning Specialist</p>
      <ul class="contact-list">
        <li class="contact-web">Website: www.holbrinathletics.example</li>
        <li class="contact-email">Email: derek@holbrinathletics.example</li>
        <li class="contact-phone">Phone:</li>
      </ul>
    </div>
  </section>
</body>
</html>
```